Plumbing company needs Business Card Design

Hi I need business card design based on logo which I uploaded. Its plumbing and heating company called Kranex Usługi Hydrauliczno-Gazowe. I want to see on my card motto of my company which is "...od wymiany uszczelki po wymiane łazienki.", my phone number, name, and website: 617248390, Marek Kowalczyk, info@kranex.org, www.kranex.org
I want to see logos of companys which I'm approved installer (Termolux) (La Valmont) (Corvo) (Pluma).
I want new creative look of business card. I like rounded corners.
Any questions please send message.
Thanks for intrest.
Business
Contact Information for Business Card
Marek Kowalczyk
617 248 390
info@kranex.org
www.kranex.org
...od wymiany uszczelki po wymiane łazienki.

```html
<!DOCTYPE html>
<html lang="pl">
<head>
<meta charset="utf-8">
<title>Kranex – wizytówka</title>
<link href="https://fonts.googleapis.com/css2?family=Oswald:wght@500;700&family=Roboto:wght@400;700&display=swap" rel="stylesheet">
<style>
  :root {
    --canvas: #e9e6e1;
    --card-white: #fbfbfb;
    --brand-red: #e3232b;
    --brand-blue: #2a4a9e;
    --brand-blue-dark: #1e3b8c;
    --brand-blue-light: #3a5fb3;
    --brand-yellow: #f6e61c;
    --ink-white: #ffffff;
  }
  * { box-sizing: border-box; margin: 0; padding: 0; }
  html, body { width: 1200px; height: 885px; overflow: hidden; }
  body {
    background: var(--canvas);
    position: relative;
    font-family: "Roboto", Arial, sans-serif;
  }
  .card {
    position: absolute;
    width: 560px;
    height: 320px;
    border-radius: 26px;
    box-shadow: 0 10px 30px rgba(0,0,0,0.18);
    overflow: hidden;
  }
  /* Front */
  .card-front {
    left: 50px; top: 140px;
    background: var(--card-white);
  }
  .brand-mark {
    position: absolute;
    display: flex; align-items: center; gap: 12px;
  }
  .brand-square {
    width: 30px; height: 30px;
    background: var(--brand-yellow);
    border-radius: 6px;
  }
  .brand-name {
    font-family: "Oswald", "Arial Narrow", sans-serif;
    font-weight: 700;
    color: var(--brand-red);
    line-height: 1;
  }
  .card-front .brand-mark { left: 40px; top: 150px; }
  .card-front .brand-name { font-size: 34px; }
  .contact {
    position: absolute;
    left: 215px; top: 70px;
  }
  .person-name {
    font-family: "Oswald", "Arial Narrow", sans-serif;
    font-weight: 700;
    font-size: 46px;
    color: var(--brand-red);
    line-height: 1.05;
  }
  .phone {
    font-family: "Oswald", "Arial Narrow", sans-serif;
    font-weight: 700;
    font-size: 36px;
    color: var(--brand-blue);
    line-height: 1.1;
    margin-top: 4px;
  }
  .contact-lines {
    display: flex; gap: 26px;
    margin-top: 16px;
  }
  .contact-line {
    display: flex; align-items: center; gap: 8px;
    font-size: 17px;
    color: var(--brand-blue);
  }
  .contact-icon {
    width: 20px; height: 20px;
    background: var(--brand-yellow);
    border-radius: 3px;
    display: flex; align-items: center; justify-content: center;
  }
  /* Back */
  .card-back {
    left: 590px; top: 440px;
    background: linear-gradient(160deg, var(--brand-blue-light) 0%, var(--brand-blue) 45%, var(--brand-blue-dark) 100%);
  }
  .card-back .brand-mark { left: 50px; top: 60px; }
  .card-back .brand-square { width: 44px; height: 44px; border-radius: 8px; }
  .card-back .brand-name { font-size: 78px; }
  .service {
    position: absolute;
    left: 50px; top: 168px;
    font-family: "Oswald", "Arial Narrow", sans-serif;
    font-weight: 500;
    font-size: 27px;
    color: var(--ink-white);
  }
  .motto {
    position: absolute;
    left: 50px; top: 222px;
    font-weight: 700;
    font-size: 20px;
    color: var(--ink-white);
  }
</style>
</head>
<body>
  <section class="card card-front" aria-label="Przód wizytówki">
    <div class="brand-mark">
      <span class="brand-square"></span>
      <span class="brand-name">Kranex</span>
    </div>
    <div class="contact">
      <h1 class="person-name">Marek Kowalczyk</h1>
      <p class="phone">617 248 390</p>
      <div class="contact-lines">
        <p class="contact-line">
          <span class="contact-icon">
            <svg width="14" height="10" viewBox="0 0 14 10"><rect x="0.5" y="0.5" width="13" height="9" fill="none" stroke="#2a4a9e"/><path d="M0.5 0.5 L7 6 L13.5 0.5" fill="none" stroke="#2a4a9e"/></svg>
          </span>
          info@kranex.org
        </p>
        <p class="contact-line">
          <span class="contact-icon">
            <svg width="14" height="14" viewBox="0 0 14 14"><circle cx="7" cy="7" r="6" fill="none" stroke="#2a4a9e"/><ellipse cx="7" cy="7" rx="2.6" ry="6" fill="none" stroke="#2a4a9e"/><line x1="1" y1="7" x2="13" y2="7" stroke="#2a4a9e"/></svg>
          </span>
          www.kranex.org
        </p>
      </div>
    </div>
  </section>

  <section class="card card-back" aria-label="Tył wizytówki">
    <div class="brand-mark">
      <span class="brand-square"></span>
      <span class="brand-name">Kranex</span>
    </div>
    <p class="service">Usługi Hydrauliczno-Gazowe</p>
    <p class="motto">wymiany uszczelki po wymiane łazienki.</p>
  </section>
</body>
</html>
```